Business Card for innovative, tech/consultant company

We are specializing in bringing together Efficiency methodology and Technology for our Business customers. We would like an astonishing business Card that matches this idea.

Target Market(s)

Businesses of medium size or more

Industry/Entity Type

Business Consultant

Contact Information for Business Card

Name, Title, personal email, www, address, phone

Font styles to use
Sans Serif

Colors
3277b5

Requirements
Must have
• - innovative, efficient design
• - good readable
• - Colors must match our logo (blue and grey)
• - the attached font (is licensed by our Company) must be used (Syntax LT)
Should not have
• overloaded

```html
<!DOCTYPE html>
<html lang="en">
<head>
<meta charset="utf-8">
<title>Veritek Business Card</title>
<link rel="stylesheet" href="https://fonts.googleapis.com/css2?family=Source+Sans+3:wght@400;600;700&display=swap">
<style>
  :root {
    --brand-blue: #0b7bbd;
    --accent-blue: #1a73b8;
    --brand-grey: #7f7f82;
    --logo-grey-light: #929295;
    --text-grey: #5e5e61;
    --band-grey: #8a8a8d;
    --card-white: #ffffff;
    --stage: #e8e5e1;
  }
  * { box-sizing: border-box; margin: 0; padding: 0; }
  html, body {
    width: 1200px;
    height: 1000px;
    overflow: hidden;
    background: var(--stage);
    font-family: "Source Sans 3", sans-serif;
  }
  .card {
    position: absolute;
    left: 265px;
    width: 665px;
    height: 397px;
    border-radius: 24px;
    overflow: hidden;
  }
  .card--front { top: 73px; background: var(--card-white); }
  .card--back { top: 532px; background: var(--brand-blue); }

  .wordmark {
    position: absolute;
    font-weight: 400;
    letter-spacing: -2px;
    line-height: 1;
    white-space: nowrap;
  }
  .card--front .wordmark {
    left: 38px;
    top: 28px;
    font-size: 118px;
    color: var(--brand-grey);
  }
  .card--back .wordmark {
    left: 0;
    right: 0;
    top: 118px;
    text-align: center;
    font-size: 150px;
    color: var(--logo-grey-light);
  }

  .name-tab {
    position: absolute;
    left: -6px;
    top: 206px;
    width: 16px;
    height: 56px;
    border-radius: 5px;
    background: var(--accent-blue);
  }
  .person { position: absolute; left: 33px; top: 208px; }
  .person__name {
    font-size: 25px;
    font-weight: 700;
    color: var(--accent-blue);
    line-height: 1.1;
  }
  .person__title {
    font-size: 17px;
    color: var(--text-grey);
    margin-top: 3px;
  }

  .contact {
    position: absolute;
    top: 300px;
    font-size: 17px;
    line-height: 25px;
    color: var(--text-grey);
  }
  .contact--address { left: 33px; }
  .contact--phones { left: 260px; }
  .contact--web { left: 472px; }
  .contact__row { display: flex; align-items: center; gap: 7px; }
  .contact__row svg { width: 14px; height: 14px; flex: none; }

  .divider {
    position: absolute;
    top: 304px;
    width: 2px;
    height: 38px;
    background: var(--accent-blue);
  }
  .divider--one { left: 229px; }
  .divider--two { left: 437px; }

  .footer-band { position: absolute; top: 373px; height: 24px; }
  .footer-band--left { left: 0; width: 173px; background: var(--band-grey); }
  .footer-band--center { left: 178px; width: 309px; background: var(--brand-blue); }
  .footer-band--right { left: 492px; width: 173px; background: var(--band-grey); }
</style>
</head>
<body>

<section class="card card--front">
  <div class="wordmark">Veritek</div>

  <div class="name-tab"></div>
  <div class="person">
    <div class="person__name">Daniel Marsh</div>
    <div class="person__title">Owner / Founder</div>
  </div>

  <div class="contact contact--address">
    <div>214 W Alder St,</div>
    <div>Brookfield, 30512</div>
  </div>

  <div class="divider divider--one"></div>

  <div class="contact contact--phones">
    <div class="contact__row">
      <svg viewBox="0 0 14 14" aria-hidden="true"><rect x="3.5" y="0.8" width="7" height="12.4" rx="1.2" fill="none" stroke="#1a73b8" stroke-width="1.4"/><line x1="6" y1="11" x2="8" y2="11" stroke="#1a73b8" stroke-width="1.2"/></svg>
      <span>+ 000 000 0000</span>
    </div>
    <div class="contact__row">
      <svg viewBox="0 0 14 14" aria-hidden="true"><path d="M1 5.2 C1 2.5 13 2.5 13 5.2 L13 6.4 L10 6.4 L10 5 L4 5 L4 6.4 L1 6.4 Z" fill="#1a73b8"/><rect x="2.5" y="7.2" width="9" height="5.5" rx="1" fill="#1a73b8"/><circle cx="7" cy="9.9" r="1.6" fill="#fff"/></svg>
      <span>+ 000 000 0000</span>
    </div>
  </div>

  <div class="divider divider--two"></div>

  <div class="contact contact--web">
    <div class="contact__row">
      <svg viewBox="0 0 14 14" aria-hidden="true"><rect x="0.8" y="2.8" width="12.4" height="8.6" fill="#1a73b8"/><path d="M1 3.2 L7 7.8 L13 3.2" fill="none" stroke="#fff" stroke-width="1.1"/></svg>
      <span>info@veritek.co.uk</span>
    </div>
    <div class="contact__row">
      <svg viewBox="0 0 14 14" aria-hidden="true"><rect x="1" y="2" width="12" height="8" fill="none" stroke="#1a73b8" stroke-width="1.5"/><rect x="4.5" y="11.5" width="5" height="1.5" fill="#1a73b8"/></svg>
      <span>www.veritek.co.uk</span>
    </div>
  </div>

  <div class="footer-band footer-band--left"></div>
  <div class="footer-band footer-band--center"></div>
  <div class="footer-band footer-band--right"></div>
</section>

<section class="card card--back">
  <div class="wordmark">Veritek</div>
</section>

</body>
</html>
```